One page (Bach and front) flyer graphic composition with all content provided

We need, by Sunday evening at the latest term, to have the enclosed page graphically worked. It will be inserted in a Fair Catalog. Dimensions 20x20We enclose logo and picture to include and draft. Don't consider the Power Point we include only to handle you content: take it from here and decide how to paste it in page to your own judgment.DLR is a software company, producing for investment market. image to give: SERIOUS, COMPETENT, STRAIGHT TO THE POINT and, most important, CREDIBLE company

Target Market(s)

Investors

Font styles to use
Serif

Colors
276eb1
0355a3
ffffff

Requirements
Must have
• Clear, strong Logo in the front page
• The picture on the back
Nice to have
• Credibility, space, clearness
Should not have
• Confusion, too much "loud"

```html
<!DOCTYPE html>
<html lang="en">
<head>
<meta charset="utf-8">
<title>DLR – Fair Catalogue Flyer</title>
<link href="https://fonts.googleapis.com/css2?family=Montserrat:wght@300;400;500;700&display=swap" rel="stylesheet">
<style>
  :root {
    --brand-blue: #276eb1;
    --brand-deep: #0355a3;
    --brand-bright: #1565c0;
    --white: #ffffff;
    --ink: #2a2a2a;
    --night: #000000;
    --page: #ffffff;
  }
  * { margin: 0; padding: 0; box-sizing: border-box; }
  html, body {
    width: 1200px; height: 903px; overflow: hidden;
    background: var(--page);
    font-family: "Montserrat", sans-serif;
  }
  .sheet { position: relative; width: 1200px; height: 903px; }
  .card {
    position: absolute; top: 175px; width: 480px; height: 480px;
    overflow: hidden;
    box-shadow: 1px 2px 4px rgba(0,0,0,0.35);
  }

  /* Front */
  .front {
    left: 86px;
    background: linear-gradient(135deg, var(--brand-blue) 0%, #2a6fc0 45%, #1d5fc4 70%, var(--brand-deep) 100%);
    color: var(--white);
  }
  .front .texture {
    position: absolute; inset: 0;
    background:
      linear-gradient(115deg, transparent 55%, rgba(255,255,255,0.06) 55%, rgba(255,255,255,0.06) 70%, transparent 70%),
      linear-gradient(160deg, transparent 40%, rgba(0,40,160,0.18) 40%, rgba(0,40,160,0.18) 60%, transparent 60%);
  }
  .front .frame {
    position: absolute; left: 15px; top: 15px; right: 15px; bottom: 15px;
    border: 1px solid rgba(255,255,255,0.85);
  }
  .front .brand {
    position: absolute; left: 38px; top: 37px;
    display: flex; align-items: center; gap: 10px;
  }
  .brand-dot { width: 72px; height: 72px; border-radius: 50%; background: var(--white); }
  .front .brand-name { font-size: 72px; font-weight: 500; line-height: 1; letter-spacing: -1px; }
  .headline { position: absolute; left: 0; top: 0; width: 100%; height: 100%; }
  .headline span { position: absolute; white-space: nowrap; line-height: 1; }
  .hl-your { left: 85px; top: 198px; font-size: 50px; font-weight: 300; }
  .hl-money { left: 84px; top: 251px; font-size: 48px; font-weight: 700; letter-spacing: 1px; }
  .hl-growth { left: 155px; top: 303px; font-size: 50px; font-weight: 300; letter-spacing: 1px; }
  .front .web { position: absolute; left: 297px; top: 428px; font-size: 23px; font-weight: 300; letter-spacing: 0.5px; }

  /* Back */
  .back { left: 626px; background: var(--white); }
  .back .night-band {
    position: absolute; left: 0; top: 0; width: 100%; height: 264px;
    background: var(--night);
  }
  .back .glass-photo {
    position: absolute; left: 254px; top: 40px; width: 200px; height: 224px;
    background: radial-gradient(ellipse at 55% 30%, #8a7a55 0%, #4a4436 30%, #1a1a18 60%, #000 80%);
  }
  .back .frame-top {
    position: absolute; left: 15px; top: 15px; right: 15px; height: 249px;
    border: 1px solid rgba(255,255,255,0.7); border-bottom: none;
  }
  .back .frame-bottom {
    position: absolute; left: 15px; top: 264px; right: 15px; bottom: 15px;
    border: 1px solid var(--brand-blue); border-top: none;
  }
  .waiting {
    position: absolute; left: 40px; top: 114px; width: 258px;
    color: var(--white); font-size: 29px; font-weight: 300; line-height: 37px; text-align: center;
    letter-spacing: 0.5px;
  }
  .invite {
    position: absolute; left: 0; top: 294px; width: 100%;
    text-align: center; color: var(--ink); font-size: 19px; font-weight: 400; line-height: 24px;
    letter-spacing: 0.3px;
  }
  .venue {
    position: absolute; left: 0; top: 361px; width: 100%;
    text-align: center; color: var(--brand-bright); font-size: 20px; font-weight: 700; letter-spacing: 0.3px;
  }
  .back .web { position: absolute; left: 54px; top: 436px; color: var(--brand-bright); font-size: 15px; font-weight: 400; }
  .back .brand { position: absolute; left: 293px; top: 417px; display: flex; align-items: center; gap: 6px; }
  .back .brand-dot { width: 40px; height: 40px; background: var(--brand-bright); }
  .back .brand-name { font-size: 42px; font-weight: 500; line-height: 1; color: var(--brand-bright); letter-spacing: -0.5px; }
</style>
</head>
<body>
<main class="sheet">
  <section class="card front" aria-label="Flyer front">
    <div class="texture" role="img" aria-label="Abstract blue network of lines and dots"></div>
    <div class="frame"></div>
    <div class="brand">
      <span class="brand-dot"></span>
      <span class="brand-name">DLR</span>
    </div>
    <h1 class="headline">
      <span class="hl-your">Your</span>
      <span class="hl-money">MONEY</span>
      <span class="hl-growth">GROWTH</span>
    </h1>
    <p class="web">www.dlrf.io</p>
  </section>

  <section class="card back" aria-label="Flyer back">
    <div class="night-band"></div>
    <div class="glass-photo" role="img" aria-label="Photo of a martini glass filled with gold coins and ice on black"></div>
    <div class="frame-top"></div>
    <div class="frame-bottom"></div>
    <p class="waiting">We are waiting<br>for you!</p>
    <p class="invite">Ask your invitation to our<br>DLR Hostess and be welcommed to:</p>
    <p class="venue">Presidential Suite Level 18</p>
    <p class="web">www.dlrf.io</p>
    <div class="brand">
      <span class="brand-dot"></span>
      <span class="brand-name">DLR</span>
    </div>
  </section>
</main>
</body>
</html>
```